Business Card Design Project

Business and Appointment Card for Medical Practice. On back of card we would like to have: blank line for patient name, Mon-Fri each with a check box next to the day, blank line for appointment date, blank line for appointment time, with option to circle am or pm.

Target Market(s)

Professional Business Associates, as well as function as patient appointment cards (on back side of card)

Industry/Entity Type

Business

Colors

Designer to choose colors to be used in the design.

```html
<!DOCTYPE html>
<html lang="en">
<head>
<meta charset="utf-8">
<title>Willowbrook Medical Associates – Business &amp; Appointment Card</title>
<link rel="stylesheet" href="https://fonts.googleapis.com/css2?family=Arimo:wght@300;400;700&family=EB+Garamond:wght@500;600&display=swap">
<style>
  :root {
    --backdrop: #e8e6e2;
    --card-white: #ffffff;
    --card-shade: #f1f1f1;
    --forest: #1f6237;
    --forest-deep: #17512c;
    --forest-light: #2a7444;
    --berry: #8e1f22;
    --ink-green: #1d5a33;
    --on-green: #ffffff;
    --on-green-soft: #dbe8df;
  }
  * { box-sizing: border-box; margin: 0; padding: 0; }
  html, body {
    width: 1200px; height: 1200px; overflow: hidden;
    background: var(--backdrop);
  }
  .canvas {
    position: relative; width: 1200px; height: 1200px;
    display: flex; flex-direction: column; align-items: center; justify-content: center; gap: 60px;
  }
  .card {
    position: relative; width: 900px; height: 514px;
    background: var(--card-white);
    box-shadow: 0 6px 20px rgba(0,0,0,0.18);
    overflow: hidden;
  }

  /* Front */
  .card-front { display: flex; }
  .brand-side {
    width: 340px; height: 100%;
    background: linear-gradient(135deg, var(--card-shade), var(--card-white) 60%);
    display: flex; align-items: center; justify-content: center; gap: 14px;
    padding: 0 24px;
  }
  .brand-dot { width: 22px; height: 22px; border-radius: 50%; background: var(--forest); flex: none; }
  .brand-name {
    font-family: "EB Garamond", Georgia, serif; font-weight: 600;
    font-size: 31px; line-height: 1.05; color: var(--berry);
  }
  .accent-stripe { width: 20px; height: 100%; background: var(--forest); }
  .accent-gap { width: 12px; height: 100%; background: var(--card-white); }
  .contact-panel {
    flex: 1; height: 100%;
    background: linear-gradient(160deg, var(--forest-deep), var(--forest) 55%, var(--forest-light));
    color: var(--on-green);
    font-family: "Arimo", Arial, sans-serif;
    padding: 56px 40px 0 56px;
  }
  .doctor-name { font-size: 40px; font-weight: 700; }
  .doctor-credentials { font-size: 30px; font-weight: 300; color: var(--on-green-soft); margin-top: 4px; letter-spacing: 1px; }
  .panel-rule { border-top: 2px dotted rgba(255,255,255,0.55); margin: 24px 0 34px; width: 380px; }
  .address { font-size: 30px; font-weight: 300; line-height: 1.3; }
  .phone { font-size: 46px; font-weight: 700; margin-top: 52px; }
  .email { font-size: 22px; font-weight: 300; margin-top: 8px; }

  /* Back */
  .card-back {
    font-family: "EB Garamond", Georgia, serif; color: var(--ink-green);
    background: linear-gradient(160deg, var(--card-white) 40%, var(--card-shade));
    padding: 46px 56px;
  }
  .appointment-title { font-size: 56px; font-weight: 600; letter-spacing: 2px; }
  .patient-line { border-top: 3px dotted var(--ink-green); margin: 22px 0 26px; }
  .weekday-row { display: flex; justify-content: space-between; font-size: 38px; font-weight: 500; }
  .weekday { display: flex; align-items: center; gap: 10px; }
  .check-box { width: 26px; height: 26px; border: 2.5px solid var(--ink-green); }
  .fill-row { display: flex; align-items: flex-end; font-size: 38px; font-weight: 500; margin-top: 34px; }
  .fill-line { border-bottom: 3px solid var(--ink-green); height: 34px; margin-left: 6px; }
  .date-line { flex: 1; }
  .time-line { width: 380px; }
  .meridiem { margin-left: 60px; font-size: 34px; }
</style>
</head>
<body>
<main class="canvas">
  <section class="card card-front" aria-label="Business card front">
    <div class="brand-side">
      <span class="brand-dot"></span>
      <span class="brand-name">Willowbrook Medical Associates</span>
    </div>
    <div class="accent-stripe"></div>
    <div class="accent-gap"></div>
    <div class="contact-panel">
      <p class="doctor-name">Dr. Ellen Hart</p>
      <p class="doctor-credentials">D.D.S.&nbsp; M.S.D</p>
      <div class="panel-rule"></div>
      <p class="address">48 Ridgeview Ln<br>Fairmont, PA 15230</p>
      <p class="phone">+1 555 210 4870</p>
      <p class="email">info@willowbrookmed.com</p>
    </div>
  </section>

  <section class="card card-back" aria-label="Appointment card back">
    <h1 class="appointment-title">Appointment for:</h1>
    <div class="patient-line"></div>
    <div class="weekday-row">
      <span class="weekday">Mon.<span class="check-box"></span></span>
      <span class="weekday">Tues.<span class="check-box"></span></span>
      <span class="weekday">Wed.<span class="check-box"></span></span>
      <span class="weekday">Thur.<span class="check-box"></span></span>
      <span class="weekday">Fri.<span class="check-box"></span></span>
    </div>
    <div class="fill-row">Date:<span class="fill-line date-line"></span></div>
    <div class="fill-row">Time:<span class="fill-line time-line"></span>
      <span class="meridiem">a.m.</span><span class="meridiem">p.m.</span>
    </div>
  </section>
</main>
</body>
</html>
```